TR Vehicular Website

We currently have a great webpage www.trvolant.ch. We realise we need a new look and have new features added:

New website: Design a new professional website with a "WOW" factor / state of the art user-friendly layout for the car industry. Keep the Corporate Identity (colors) of EQ  Motors and restructure the current menus and webdesign to categorize into products and services. some of the subpages create new, others include our existing ones.

 

Products:

1. New Cars (subpage just include existing one)

2. Used Cars (subpage just include existing one)

3. Car parts (subpage shop just include existing one)

 

Services:

1. Car wrapping/ folierung (create new subpage leveraging on existing one)

2. car rental (create new subpage and include existing car rental portal)

3. Fahrzeugaufbereitung/ car washing (create new subpage)

4. Import / export services (create new subpage)

5. Mechanics & installation and maintenance services (create new subpage)

6. bump fixing (create new subpage)

 

Structural / layout guidance for design, pls see enclosed. Design-wise, pls show us better than this.

 

Target Market(s)

Car Owners

Industry/Entity Type

Automotive

Number of Pages Required

4 page

Requirements
Must have
• Theme colours : red, black & white
• With codings.
• We would like to see how each sub links look like as whole websites.
• We can build up for further discussion on development with the winner.
Nice to have
• An eye catching promotions box, using some sort of "Flash"

```html
<!DOCTYPE html>
<html lang="en">
<head>
<meta charset="utf-8">
<title>TR Vehicular – Home</title>
<link href="https://fonts.googleapis.com/css2?family=Open+Sans:wght@400;600;700;800&family=Oswald:wght@400;500&display=swap" rel="stylesheet">
<style>
:root{
  --red:#c8161d;
  --red-dark:#a50f15;
  --ink:#1e1e1e;
  --dark:#2a2a2a;
  --darker:#1b1b1b;
  --grey:#f1f1f1;
  --mid:#8a8a8a;
  --line:#dcdcdc;
  --white:#ffffff;
}
*{box-sizing:border-box;margin:0;padding:0}
html,body{width:1200px;height:2636px;overflow:hidden;background:var(--white)}
body{font-family:"Open Sans",Arial,sans-serif;color:var(--ink);position:relative}
.heading{font-family:"Oswald","Arial Narrow",sans-serif;text-transform:uppercase}

/* header */
.site-header{position:absolute;top:0;left:0;width:1200px;height:90px;background:var(--white);border-bottom:1px solid var(--line)}
.brand{position:absolute;left:40px;top:14px;display:flex;align-items:center;gap:10px}
.brand-dot{width:16px;height:16px;border-radius:50%;background:var(--red)}
.brand-name{font-size:30px;font-weight:700;color:var(--ink);letter-spacing:-.5px;line-height:1.2}
.brand-tagline{position:absolute;left:66px;top:56px;font-size:10px;color:var(--mid)}
.utility{position:absolute;right:40px;top:10px;display:flex;gap:8px;align-items:center}
.social{width:22px;height:22px;background:#e3e3e3;border-radius:2px}
.search,.lang{height:22px;border:1px solid var(--line);font-size:10px;color:var(--mid);padding:4px 8px;width:110px;line-height:12px}
.lang{width:100px;position:relative}
.lang::after{content:"";position:absolute;right:8px;top:8px;border:4px solid transparent;border-top-color:var(--mid)}
.main-nav{position:absolute;right:40px;top:48px;display:flex}
.main-nav a{font-size:12px;font-weight:600;color:var(--ink);text-decoration:none;padding:12px 16px 14px;text-transform:uppercase}
.main-nav a.active{color:var(--red);border-bottom:3px solid var(--red)}

/* hero */
.hero{position:absolute;top:90px;left:0;width:1200px;height:420px;overflow:hidden;
  background:
    radial-gradient(ellipse 260px 180px at 190px 200px,rgba(255,255,255,.95),rgba(230,233,236,.6) 45%,rgba(230,233,236,0) 75%),
    radial-gradient(ellipse 480px 300px at 280px 260px,rgba(196,202,208,.9),rgba(196,202,208,0) 70%),
    radial-gradient(ellipse 520px 180px at 880px 90px,rgba(18,20,24,.85),rgba(18,20,24,0) 70%),
    radial-gradient(ellipse 420px 160px at 1000px 230px,rgba(150,158,166,.55),rgba(150,158,166,0) 70%),
    linear-gradient(180deg,#5d646b 0%,#3e444a 45%,#2f3337 70%,#1d2023 100%)}
.hero-road{position:absolute;left:0;right:0;bottom:0;height:120px;
  background:linear-gradient(180deg,rgba(60,66,60,0) 0%,rgba(52,62,44,.7) 35%,#2a2c2e 60%,#1a1b1d 100%)}
.hero-visual{position:absolute;inset:0}
.hero-copy{position:absolute;left:716px;top:170px;width:450px}
.hero-title{font-size:29px;font-weight:500;color:var(--white);line-height:1.25;text-shadow:0 2px 6px rgba(0,0,0,.4)}
.hero-actions{margin-top:22px;display:flex;gap:10px}
.btn{display:inline-block;font-size:11px;font-weight:700;text-transform:uppercase;padding:9px 16px;color:var(--white)}
.btn-red{background:var(--red)}
.btn-dark{background:rgba(0,0,0,.6)}
.hero-dots{position:absolute;left:50%;bottom:28px;transform:translateX(-50%);display:flex;gap:8px}
.hero-dots span{width:9px;height:9px;border-radius:50%;background:rgba(255,255,255,.5)}
.hero-dots span.on{background:var(--white)}

/* products */
.products{position:absolute;top:500px;left:0;width:1200px;height:460px;background:var(--grey);display:flex;gap:38px;padding:0 40px}
.product-card{width:350px;height:430px;background:var(--red);box-shadow:0 6px 14px rgba(0,0,0,.22);position:relative;z-index:1}
.product-card h2{height:56px;line-height:56px;text-align:center;color:var(--white);font-size:26px;font-weight:500}
.product-image{height:244px}
.img-newcar{background:
  radial-gradient(ellipse 150px 70px at 170px 150px,#f7a13a,#e4761d 55%,rgba(228,118,29,0) 100%),
  radial-gradient(ellipse 200px 40px at 175px 205px,rgba(40,40,40,.55),rgba(40,40,40,0) 80%),
  linear-gradient(180deg,#f4f4f4 0%,#e6e6e6 60%,#cfcfcf 100%)}
.img-usedcar{background:
  radial-gradient(ellipse 170px 80px at 175px 140px,#3a3c40,#15161a 60%,rgba(21,22,26,0) 100%),
  radial-gradient(ellipse 120px 30px at 190px 110px,rgba(220,225,230,.5),rgba(220,225,230,0) 80%),
  linear-gradient(180deg,#e2e2e2 0%,#9a9a9a 55%,#3e3e3e 100%)}
.img-parts{background:
  radial-gradient(circle 90px at 180px 125px,#2b2b2b,#101010 70%,rgba(16,16,16,0) 100%),
  radial-gradient(circle 60px at 80px 180px,#2a2a2a,#111 70%,rgba(17,17,17,0) 100%),
  radial-gradient(circle 60px at 280px 180px,#2a2a2a,#111 70%,rgba(17,17,17,0) 100%),
  linear-gradient(180deg,#fbfbfb,#ececec)}
.product-card p{color:var(--white);font-size:11px;line-height:1.6;padding:24px 26px;text-align:center}

/* partners */
.partners{position:absolute;top:990px;left:40px;width:1120px;height:96px;border:1px solid var(--line);display:flex;justify-content:space-around;align-items:center;padding:0 20px}
.partner{height:22px;border-radius:11px;background:linear-gradient(180deg,#c4c4c4,#9c9c9c)}
.partner.w1{width:46px}.partner.w2{width:38px;height:28px;border-radius:14px}.partner.w3{width:52px;height:18px;border-radius:9px}.partner.w4{width:30px;height:30px;border-radius:50%}

/* services */
.services-title{position:absolute;top:1166px;left:40px;font-size:22px;color:var(--red);font-weight:500}
.services{position:absolute;top:1232px;left:40px;width:1120px;display:flex;gap:10px}
.service-card{width:216px;height:440px;background:var(--dark);position:relative;color:var(--white)}
.service-card h3{font-size:15px;font-weight:500;padding:12px 40px 0 12px;height:58px;line-height:1.25}
.service-image{height:176px}
.service-card p{font-size:10px;line-height:1.6;color:#bdbdbd;padding:14px 12px 8px}
.service-link{font-size:10px;font-weight:700;padding:4px 12px;text-transform:uppercase}
.service-cta{position:absolute;left:0;right:0;bottom:0;height:36px;line-height:36px;background:var(--red);font-size:11px;font-weight:700;padding-left:12px;text-transform:uppercase}
.img-wrap{background:radial-gradient(ellipse 90px 40px at 110px 110px,#2b2b2b,#0f0f0f 65%,rgba(15,15,15,0) 100%),linear-gradient(180deg,#9a9a9a,#5a5a5a 60%,#333)}
.img-rental{background:radial-gradient(ellipse 80px 30px at 70px 120px,rgba(70,80,95,.8),rgba(70,80,95,0)),radial-gradient(ellipse 80px 30px at 160px 115px,rgba(160,160,165,.9),rgba(160,160,165,0)),linear-gradient(180deg,#dfe4e8,#a8adb1 60%,#6c6f72)}
.img-wash{background:radial-gradient(ellipse 90px 60px at 120px 80px,#f2f5f8,rgba(242,245,248,0) 80%),linear-gradient(160deg,#9fb4c6,#5f7588 60%,#3b4a57)}
.img-import{background:radial-gradient(ellipse 100px 60px at 100px 70px,#f2d188,rgba(242,209,136,0) 80%),linear-gradient(180deg,#d9a94f,#9c6f2c 60%,#4a3a22)}
.img-mech{background:radial-gradient(ellipse 80px 50px at 80px 110px,#c9bfa6,rgba(201,191,166,0) 80%),linear-gradient(160deg,#8d8674,#4c4639 60%,#2a2720)}

/* gallery */
.gallery{position:absolute;top:1722px;left:40px;width:1120px;height:150px;display:flex;gap:8px}
.gallery-tile{flex:1;position:relative}
.gallery-caption{position:absolute;left:0;right:0;bottom:0;background:rgba(0,0,0,.75);color:var(--white);font-size:11px;padding:6px 10px}
.img-crowd{background:radial-gradient(ellipse 120px 50px at 130px 95px,#c2b19a,rgba(194,177,154,0) 80%),linear-gradient(180deg,#6f6152,#3a3129)}
.img-vans{background:radial-gradient(ellipse 130px 40px at 140px 80px,#fff,rgba(255,255,255,0) 80%),linear-gradient(180deg,#e8e8e8,#8c8c8c 70%,#505050)}
.img-ad{background:radial-gradient(ellipse 100px 40px at 150px 90px,#7a7a7a,rgba(122,122,122,0) 80%),linear-gradient(180deg,#3c3c3c,#121212)}
.img-showroom{background:radial-gradient(ellipse 110px 35px at 160px 105px,#6d6f72,rgba(109,111,114,0) 80%),linear-gradient(180deg,#fafafa,#d4d4d4 60%,#a8a8a8)}

/* testimonial + video */
.testimonial{position:absolute;top:1912px;left:40px;width:540px;height:248px;background:var(--grey);padding:28px 30px}
.quote-mark{position:absolute;left:28px;top:24px;width:34px;height:26px}
.testimonial blockquote{margin-left:56px;font-size:11px;line-height:1.7;color:#555}
.testimonial-author{position:absolute;right:30px;bottom:30px;font-size:11px;font-style:italic;color:#555}
.testimonial-arrows{position:absolute;left:30px;bottom:28px;display:flex;gap:4px}
.testimonial-arrows span{width:20px;height:20px;background:#555;display:flex;align-items:center;justify-content:center}
.testimonial-arrows span.on{background:var(--red)}
.video{position:absolute;top:1912px;left:628px;width:532px;height:248px;
  background:radial-gradient(ellipse 160px 60px at 200px 200px,#b63126,rgba(182,49,38,0) 80%),
  radial-gradient(ellipse 300px 90px at 260px 60px,#e8e2d4,rgba(232,226,212,0) 80%),
  linear-gradient(180deg,#bdb39d 0%,#8a8c74 45%,#5d5a4c 100%)}
.video-play{position:absolute;left:50%;top:50%;transform:translate(-50%,-50%)}

/* footer */
.site-footer{position:absolute;top:2210px;left:0;width:1200px;height:310px;background:var(--dark);color:var(--white);display:flex;gap:40px;padding:48px 40px 0}
.footer-col{width:250px}
.footer-col h4{font-size:17px;font-weight:500;margin-bottom:18px}
.hours li{list-style:none;font-size:10px;color:#aaa;line-height:1.9}
.contact-row{display:flex;gap:10px;font-size:10px;color:#aaa;line-height:1.6;margin-bottom:14px}
.contact-row svg{flex:none;margin-top:2px}
.tweet{display:flex;gap:10px;font-size:10px;color:#aaa;line-height:1.6;margin-bottom:22px}
.tweet a{color:var(--red)}
.footer-head{display:flex;justify-content:space-between;align-items:baseline}
.newsletter p{font-size:10px;color:#aaa;line-height:1.6;margin-bottom:22px}
.newsletter-form{display:flex}
.newsletter-input{width:200px;height:30px;background:var(--white);font-size:10px;color:var(--mid);padding:8px}
.newsletter-send{width:30px;height:30px;background:var(--red);display:flex;align-items:center;justify-content:center}

/* bottom bar */
.bottom-bar{position:absolute;top:2520px;left:0;width:1200px;height:116px;background:var(--darker)}
.bottom-bar .brand-name{color:var(--white);font-size:26px}
.bottom-bar .brand{top:40px}
.bottom-nav{position:absolute;right:40px;top:50px;display:flex;gap:34px}
.bottom-nav a{font-size:11px;color:#bbb;text-decoration:none;text-transform:uppercase}
</style>
</head>
<body>

<header class="site-header">
  <div class="brand"><span class="brand-dot"></span><span class="brand-name">TR Volant</span></div>
  <div class="brand-tagline">Automotive · Services · Zurich · Basel</div>
  <div class="utility">
    <span class="social"></span><span class="social"></span><span class="social"></span>
    <div class="search">SEARCH</div>
    <div class="lang">ENGLISH</div>
  </div>
  <nav class="main-nav">
    <a class="active" href="#">Home</a><a href="#">Products</a><a href="#">Services</a><a href="#">Car Wrapping</a><a href="#">Enquiry</a><a href="#">About Us</a><a href="#">Store</a>
  </nav>
</header>

<section class="hero">
  <div class="hero-visual" role="img" aria-label="Close-up of a silver sports car headlight on a wet road under a stormy sky"></div>
  <div class="hero-road"></div>
  <div class="hero-copy">
    <h1 class="hero-title heading">Lorem ipsum is simply dummy text of the printing</h1>
    <div class="hero-actions"><span class="btn btn-red">Find out more</span><span class="btn btn-dark">Book now</span></div>
  </div>
  <div class="hero-dots"><span class="on"></span><span></span><span></span></div>
</section>

<section class="products">
  <article class="product-card">
    <h2 class="heading">New Cars</h2>
    <div class="product-image img-newcar" role="img" aria-label="Orange sports car on a light studio floor"></div>
    <p>Sed ut perspiciatis unde omnis iste natus error sit voluptatem accusantium doloremque laudantium, totam rem aperiam.</p>
  </article>
  <article class="product-card">
    <h2 class="heading">Usedcars</h2>
    <div class="product-image img-usedcar" role="img" aria-label="Black saloon car on a grey background"></div>
    <p>Sed ut perspiciatis unde omnis iste natus error sit voluptatem accusantium doloremque laudantium, totam rem aperiam.</p>
  </article>
  <article class="product-card">
    <h2 class="heading">Car Parts</h2>
    <div class="product-image img-parts" role="img" aria-label="Stack of new car tyres on white"></div>
    <p>Sed ut perspiciatis unde omnis iste natus error sit voluptatem accusantium doloremque laudantium, totam rem aperiam.</p>
  </article>
</section>

<section class="partners" aria-label="Car brands we work with">
  <span class="partner w1"></span><span class="partner w2"></span><span class="partner w1"></span><span class="partner w4"></span><span class="partner w3"></span>
  <span class="partner w2"></span><span class="partner w3"></span><span class="partner w4"></span><span class="partner w1"></span><span class="partner w2"></span>
</section>

<h2 class="services-title heading">Our Services</h2>
<section class="services">
  <article class="service-card">
    <h3 class="heading">Car Wrapping</h3>
    <div class="service-image img-wrap" role="img" aria-label="Black wrapped car"></div>
    <p>Nemo enim ipsam voluptatem quia voluptas sit aspernatur aut odit aut fugit sed quia.</p>
    <div class="service-link">View products</div>
    <div class="service-cta">Send enquiry</div>
  </article>
  <article class="service-card">
    <h3 class="heading">Car Rental</h3>
    <div class="service-image img-rental" role="img" aria-label="Row of rental cars in a lot"></div>
    <p>Nemo enim ipsam voluptatem quia voluptas sit aspernatur aut odit aut fugit sed quia.</p>
    <div class="service-link">View products</div>
    <div class="service-cta">Book now</div>
  </article>
  <article class="service-card">
    <h3 class="heading">Car Washing</h3>
    <div class="service-image img-wash" role="img" aria-label="Car being washed with foam"></div>
    <p>Nemo enim ipsam voluptatem quia voluptas sit aspernatur aut odit aut fugit sed quia.</p>
    <div class="service-link">View products</div>
    <div class="service-cta">Book now</div>
  </article>
  <article class="service-card">
    <h3 class="heading">Import / Export Administration</h3>
    <div class="service-image img-import" role="img" aria-label="Cars loaded for shipping at sunset"></div>
    <p>Nemo enim ipsam voluptatem quia voluptas sit aspernatur aut odit aut fugit sed quia.</p>
    <div class="service-link">View products</div>
    <div class="service-cta">Send enquiry</div>
  </article>
  <article class="service-card">
    <h3 class="heading">Car Mechanics&amp; Maintenance</h3>
    <div class="service-image img-mech" role="img" aria-label="Mechanic working on an engine"></div>
    <p>Nemo enim ipsam voluptatem quia voluptas sit aspernatur aut odit aut fugit sed quia.</p>
    <div class="service-link">View products</div>
    <div class="service-cta">Send enquiry</div>
  </article>
</section>

<section class="gallery">
  <div class="gallery-tile img-crowd" role="img" aria-label="Crowd gathered around a car at an event"></div>
  <div class="gallery-tile img-vans" role="img" aria-label="Delivery vans parked in a row">
    <div class="gallery-caption">40 Brilliant and Mind Blowing Car Advertisements</div>
  </div>
  <div class="gallery-tile img-ad" role="img" aria-label="Dark car advertisement scene"></div>
  <div class="gallery-tile img-showroom" role="img" aria-label="Silver car in a bright showroom"></div>
</section>

<section class="testimonial">
  <svg class="quote-mark" viewBox="0 0 34 26"><path d="M0 26V14C0 6 4 1 12 0v5c-4 1-6 4-6 8h6v13zM20 26V14c0-8 4-13 12-14v5c-4 1-6 4-6 8h6v13z" fill="#cfcfcf"/></svg>
  <blockquote>Sed ut perspiciatis unde omnis iste natus error sit voluptatem accusantium doloremque laudantium, totam rem aperiam, eaque ipsa quae ab illo inventore veritatis et quasi architecto beatae vitae dicta sunt explicabo.</blockquote>
  <div class="testimonial-arrows">
    <span><svg width="8" height="8" viewBox="0 0 8 8"><path d="M6 0L2 4l4 4" fill="none" stroke="#fff" stroke-width="1.5"/></svg></span>
    <span class="on"><svg width="8" height="8" viewBox="0 0 8 8"><path d="M2 0l4 4-4 4" fill="none" stroke="#fff" stroke-width="1.5"/></svg></span>
  </div>
  <div class="testimonial-author">Lena Moser</div>
</section>

<section class="video" role="img" aria-label="Video still of a red convertible driving on a country road">
  <svg class="video-play" width="70" height="70" viewBox="0 0 70 70"><circle cx="35" cy="35" r="33" fill="rgba(0,0,0,.35)" stroke="#fff" stroke-width="3"/><path d="M28 22l20 13-20 13z" fill="#fff"/></svg>
</section>

<footer class="site-footer">
  <div class="footer-col">
    <h4 class="heading">Working Hours</h4>
    <ul class="hours">
      <li>Mon : 08.00 – 18.00</li><li>Tue : 08.00 – 18.00</li><li>Wed : 08.00 – 18.00</li>
      <li>Thu : 08.00 – 18.00</li><li>Fri : 08.00 – 17.00</li><li>Sat : 09.00 – 13.00</li>
    </ul>
  </div>
  <div class="footer-col">
    <h4 class="heading">Contact Us</h4>
    <div class="contact-row"><svg width="12" height="14" viewBox="0 0 12 14"><path d="M6 0a5 5 0 0 0-5 5c0 4 5 9 5 9s5-5 5-9a5 5 0 0 0-5-5zm0 7a2 2 0 1 1 0-4 2 2 0 0 1 0 4z" fill="#888"/></svg><span>Werkstrasse 12, 8400 Winterthur,<br>Switzerland</span></div>
    <div class="contact-row"><svg width="12" height="12" viewBox="0 0 12 12"><path d="M2 0l3 3-1.5 2a7 7 0 0 0 3.5 3.5L9 7l3 3-2 2C5 12 0 7 0 2z" fill="#888"/></svg><span>+41 52 000 00 00</span></div>
    <div class="contact-row"><svg width="12" height="10" viewBox="0 0 12 10"><rect x="0.5" y="0.5" width="11" height="9" fill="none" stroke="#888"/><path d="M1 1l5 4 5-4" fill="none" stroke="#888"/></svg><span>info@trvolant.ch</span></div>
  </div>
  <div class="footer-col">
    <div class="footer-head"><h4 class="heading">Latest Tweets</h4><span style="font-size:12px;color:#aaa">‹ &nbsp; ›</span></div>
    <div class="tweet"><span style="color:#888">•</span><span>Lorem ipsum dolor sit amet consectetur adipiscing elit sed do eiusmod tempor <a>t.co/trv01</a></span></div>
    <div class="tweet"><span style="color:#888">•</span><span>Lorem ipsum dolor sit amet consectetur adipiscing elit sed do eiusmod tempor <a>t.co/trv02</a></span></div>
  </div>
  <div class="footer-col newsletter">
    <h4 class="heading">Newsletter</h4>
    <p>Sign up to receive our latest offers, service news and seasonal promotions by email.</p>
    <div class="newsletter-form">
      <div class="newsletter-input">Your email address</div>
      <div class="newsletter-send"><svg width="8" height="10" viewBox="0 0 8 10"><path d="M1 0l6 5-6 5" fill="none" stroke="#fff" stroke-width="2"/></svg></div>
    </div>
  </div>
</footer>

<div class="bottom-bar">
  <div class="brand"><span class="brand-dot"></span><span class="brand-name">TR Volant</span></div>
  <nav class="bottom-nav">
    <a href="#">Home</a><a href="#">Products</a><a href="#">Services</a><a href="#">Car Wrapping</a><a href="#">Enquiry</a><a href="#">About Us</a><a href="#">Store</a>
  </nav>
</div>

</body>
</html>
```